Information Security Company Business Cards

Using our included logo, we need a business card design. It should have standard contact information such as :

Ravi Tanner
Senior Security Engineer
ravi.tanner@quorvex-hub.com
877.640.3958

Maybe include the website "www.quorvex-hub.com" that we will be redesigning soon.??

open to suggestions of course...

Target Market(s)

Our customers are small to large companies. Generally health-care, financial, insurance and the like.

Industry/Entity Type

Business

Font styles to use
Other font styles liked:
• Something that works with the logo

Requirements
Must have
• Colors should flow with the logo if possible. Or at least we think it should.

```html
<!DOCTYPE html>
<html lang="en">
<head>
<meta charset="utf-8">
<title>Quorvex Hub Business Cards</title>
<link rel="stylesheet" href="https://fonts.googleapis.com/css2?family=Open+Sans:wght@400;600;700&family=Roboto:wght@400;500&display=swap">
<style>
  :root {
    --bg: #e6e6e8;
    --card: #ffffff;
    --card-shade: #e9e9ec;
    --brand-blue: #0f0f9c;
    --brand-navy: #13137a;
    --charcoal: #3a3a3c;
    --text-grey: #333336;
    --white: #ffffff;
  }
  * { box-sizing: border-box; margin: 0; padding: 0; }
  html, body { width: 1200px; height: 1200px; overflow: hidden; }
  body {
    background: var(--bg);
    font-family: "Open Sans", Arial, sans-serif;
    position: relative;
  }
  .card {
    position: absolute;
    left: 180px;
    width: 840px;
    height: 480px;
    background: radial-gradient(ellipse at 40% 40%, var(--card) 55%, var(--card-shade) 100%);
    box-shadow: 0 8px 24px rgba(0,0,0,0.18);
    overflow: hidden;
  }
  .card--contact { top: 90px; }
  .card--brand { top: 630px; }

  /* contact side */
  .identity {
    position: absolute;
    left: 52px;
    top: 92px;
    display: flex;
    align-items: center;
    gap: 18px;
  }
  .identity__mark {
    width: 92px; height: 92px;
    border-radius: 50%;
    border: 10px solid var(--charcoal);
  }
  .identity__name {
    font-weight: 700;
    font-size: 36px;
    line-height: 0.95;
    color: var(--brand-blue);
    text-transform: uppercase;
    letter-spacing: 1px;
  }
  .person {
    position: absolute;
    right: 58px;
    top: 44px;
    font-family: "Roboto", Arial, sans-serif;
  }
  .person__name {
    font-size: 34px;
    color: var(--brand-navy);
    font-weight: 400;
  }
  .person__role {
    font-size: 22px;
    color: var(--text-grey);
    margin-top: 8px;
  }
  .divider {
    position: absolute;
    left: 0; right: 0;
    top: 236px;
    height: 9px;
    background: var(--charcoal);
  }
  .contact-band {
    position: absolute;
    left: 0; right: 0;
    top: 245px;
    height: 190px;
    background: var(--brand-blue);
    padding: 34px 0 0 48px;
  }
  .contact-list { list-style: none; }
  .contact-list li {
    display: flex;
    align-items: center;
    gap: 14px;
    color: var(--white);
    font-size: 25px;
    line-height: 46px;
  }
  .contact-list svg { width: 22px; height: 22px; flex: none; }

  /* brand side */
  .brand-mark {
    position: absolute;
    left: 40px;
    top: 30px;
    width: 400px;
    height: 400px;
    border-radius: 50%;
    border: 26px solid var(--charcoal);
  }
  .brand-name {
    position: absolute;
    left: 490px;
    top: 150px;
    font-weight: 700;
    font-size: 58px;
    line-height: 1;
    color: var(--brand-blue);
    text-transform: uppercase;
    letter-spacing: 2px;
  }
  .web-tag {
    position: absolute;
    right: 0;
    top: 396px;
    width: 340px;
    height: 46px;
    background: var(--brand-blue);
    color: var(--white);
    font-size: 22px;
    line-height: 46px;
    padding-left: 18px;
  }
</style>
</head>
<body>
  <section class="card card--contact">
    <div class="identity">
      <div class="identity__mark"></div>
      <div class="identity__name">Quorvex<br>Hub</div>
    </div>
    <div class="person">
      <div class="person__name">Ravi Tanner</div>
      <div class="person__role">Senior Security Engineer</div>
    </div>
    <div class="divider"></div>
    <div class="contact-band">
      <ul class="contact-list">
        <li>
          <svg viewBox="0 0 24 24" aria-hidden="true"><rect x="2" y="5" width="20" height="14" fill="#fff"/><path d="M2 5l10 8 10-8" fill="none" stroke="#0f0f9c" stroke-width="2"/></svg>
          ravi.tanner@quorvex-hub.com
        </li>
        <li>
          <svg viewBox="0 0 24 24" aria-hidden="true"><path d="M6.6 2.5l3 3.5-2 2.6c1.3 2.8 3.6 5.1 6.4 6.4l2.6-2 3.5 3-1.6 3.5C10.5 19.5 4.5 13.5 3.1 4.1z" fill="#fff"/></svg>
          877.640.3958
        </li>
        <li>
          <svg viewBox="0 0 24 24" aria-hidden="true" fill="none" stroke="#fff" stroke-width="2"><circle cx="12" cy="12" r="10"/><ellipse cx="12" cy="12" rx="4.5" ry="10"/><path d="M2 12h20M4 7h16M4 17h16"/></svg>
          www.quorvex-hub.com
        </li>
      </ul>
    </div>
  </section>

  <section class="card card--brand">
    <div class="brand-mark"></div>
    <div class="brand-name">Quorvex<br>Hub</div>
    <div class="web-tag">www.quorvex-hub.com</div>
  </section>
</body>
</html>
```